Tin Lantern "Cold Harbor" New Single Cover

Create cover artwork for the band Tin Lantern' new single "Cold Harbor" being released early 2020. Style, font and graphics to be consistent with band's previous releases and overall brand identity. Visit www.tinlanternband.example and our Spotify page https://listen.tunevault.example/artist/8QXzrT4LmNbW2cPd7KeYjA?si=HVkR3sTpZ9wLqYb2nMcXuE to view our previous releases and overall brand identity. Some examples attached as well. We are looking for someone to work with on future projects as well.

Lyrics are here: https://pages.draftbox.example/document/d/7KpRw2mXn_9LqTe4Zs8Vd_HyjB2cF5t03Qa71nRkwLpY/edit

Music is here: https://wavecrate.example/tinlantern/cold-harbor/s-rbmtx

Font styles to use
Sans Serif

Colors

Designer to choose colors to be used in the design.

Requirements
Must have
• Must be consistent with current brand identity and with prior album / single art.

```html
<!DOCTYPE html>
<html lang="en">
<head>
<meta charset="utf-8">
<title>Tin Lantern — Cold Harbor Single Cover</title>
<link rel="stylesheet" href="https://fonts.googleapis.com/css2?family=Josefin+Sans:wght@400;600&display=swap">
<style>
  :root {
    --backdrop: #4a4a4a;
    --cover-light: #f7b81e;
    --cover-dark: #ef9a14;
    --ink: #1b2a5c;
    --ornament-tone: rgba(27, 42, 92, 0.10);
  }
  html, body {
    margin: 0;
    padding: 0;
    width: 1200px;
    height: 960px;
    overflow: hidden;
    background: var(--backdrop);
  }
  .canvas {
    position: relative;
    width: 1200px;
    height: 960px;
    background: var(--backdrop);
  }
  .cover {
    position: absolute;
    left: 170px;
    top: 50px;
    width: 860px;
    height: 860px;
    background: radial-gradient(circle at 48% 45%, var(--cover-light) 0%, var(--cover-dark) 85%);
    color: var(--ink);
    font-family: "Josefin Sans", sans-serif;
  }
  .ornament {
    position: absolute;
    border-radius: 14px;
    background: var(--ornament-tone);
  }
  .ornament--burst {
    left: 38%;
    top: 15%;
    width: 23%;
    height: 11%;
  }
  .ornament--curl-left {
    left: 14%;
    top: 55%;
    width: 10%;
    height: 6%;
  }
  .ornament--curl-right {
    left: 72%;
    top: 55%;
    width: 10%;
    height: 6%;
  }
  .single-title {
    position: absolute;
    left: 0;
    right: 0;
    top: 28%;
    margin: 0;
    text-align: center;
    font-weight: 400;
    font-size: 140px;
    line-height: 0.94;
    letter-spacing: 0.01em;
    text-transform: uppercase;
  }
  .single-title span {
    display: block;
  }
  .band-name {
    position: absolute;
    left: 0;
    right: 0;
    top: 83%;
    margin: 0;
    text-align: center;
    font-weight: 600;
    font-size: 46px;
    letter-spacing: 0.16em;
    text-transform: uppercase;
  }
</style>
</head>
<body>
  <main class="canvas">
    <section class="cover">
      <div class="ornament ornament--burst" role="img" aria-label="Hand-drawn burst of short rays above the title"></div>
      <h1 class="single-title"><span>Cold</span><span>Harbor</span></h1>
      <div class="ornament ornament--curl-left" role="img" aria-label="Hand-drawn looping flourish beside the title"></div>
      <div class="ornament ornament--curl-right" role="img" aria-label="Hand-drawn looping flourish beside the title"></div>
      <p class="band-name">Tin Lantern</p>
    </section>
  </main>
</body>
</html>
```